Event Poster for Bar Sunday Live Music and Happy Hour

We are a bar. Every Sunday we have a HARBOUR HOURS event where we have live music and a Sunday Happy Hour. I would like a poster that promotes this weekly event in A4 and A3. Information the poster should include:Event Name: SUNDAY SESSIONSVenue: Copper Lantern 218-222 Marlow Rd PrestonDrink Specials: 3:00 pm - 5:00pmLive Music: 4:30pm -6:30pmAttached is our logo.

Target Market(s)

Both sexes 30-40 year olds

Industry/Entity Type

Hospitality

Font styles to use
Sans Serif

Colors

Designer to choose colors to be used in the design.

Requirements
Must have
• Event Name: HARBOUR HOURS
• Venue: Copper Lantern 218-222 Marlow Rd Preston
• Drink Specials: 3:00 pm - 5:00pm
• Live Music: 4:30pm -6:30pm
• Logo
Nice to have
• Open to different styles and ideas. Like colour.
Should not have
• It should not be too blokey are over the top bar-like.

```html
<!DOCTYPE html>
<html lang="en">
<head>
<meta charset="utf-8">
<title>Harbour Hours – Copper Lantern</title>
<link href="https://fonts.googleapis.com/css2?family=Oswald:wght@300;400;600&family=Josefin+Sans:wght@300&display=swap" rel="stylesheet">
<style>
  :root {
    --backdrop: #bcbcbc;
    --poster: #050507;
    --wall: #1b1b1e;
    --neon-warm-fill: #ffe6cf;
    --neon-red: #ff2a1a;
    --neon-orange: #ff8a2a;
    --neon-blue: #3f7bff;
    --neon-violet: #9a5cff;
    --white: #f4f4f4;
    --amber: #f2a23a;
  }
  * { margin: 0; padding: 0; box-sizing: border-box; }
  html, body { width: 1150px; height: 1200px; overflow: hidden; }
  body { background: var(--backdrop); position: relative; font-family: "Oswald", sans-serif; }

  .poster {
    position: absolute; left: 162px; top: 20px;
    width: 826px; height: 1161px;
    background: var(--poster); overflow: hidden;
  }
  .wall-photo {
    position: absolute; left: 0; top: 0; width: 826px; height: 720px;
    background:
      radial-gradient(ellipse 260px 200px at 430px 170px, #2d2d31 0%, transparent 70%),
      linear-gradient(180deg, #26262a 0%, var(--wall) 45%, var(--poster) 100%);
  }
  .studio-mic-photo {
    position: absolute; left: 11px; top: 0; width: 124px; height: 313px;
    background: linear-gradient(90deg, #3a3a3d 0%, #b9b9bb 35%, #8d8d90 60%, #2c2c2f 100%);
    border-radius: 0 0 10px 10px; opacity: .85;
  }
  .glass-mic-photo {
    position: absolute; left: 275px; top: 707px; width: 551px; height: 454px;
    background:
      radial-gradient(circle 48px at 120px 130px, #f3b431 0%, #d98a12 70%, transparent 72%),
      radial-gradient(ellipse 120px 70px at 200px 270px, #2f56d8 0%, #14225e 70%, transparent 100%),
      radial-gradient(ellipse 110px 150px at 440px 170px, #7a57b8 0%, #2a1c4a 60%, transparent 100%),
      linear-gradient(180deg, transparent 0%, #0a0718 100%);
  }

  .brand-mark {
    position: absolute; left: 302px; top: 100px; width: 222px; height: 222px;
    border: 2px solid var(--white); border-radius: 50%; background: #000;
    display: flex; align-items: center; justify-content: center; text-align: center;
  }
  .brand-name {
    font-family: "Oswald", sans-serif; font-weight: 300; font-size: 30px;
    color: var(--white); letter-spacing: 3px; line-height: 1.15; text-transform: uppercase;
  }

  .title { position: absolute; left: 0; width: 826px; text-align: center; line-height: 1; text-transform: uppercase; }
  .title-top {
    top: 340px; font-weight: 300; font-size: 175px; color: var(--neon-warm-fill);
    text-shadow: 0 0 4px var(--neon-orange), 0 0 14px var(--neon-red), 0 0 30px var(--neon-red);
  }
  .title-bottom {
    top: 510px; font-weight: 600; font-size: 172px;
    color: #6f86ff;
    background: linear-gradient(90deg, var(--neon-blue) 0%, var(--neon-violet) 45%, var(--neon-blue) 100%);
    -webkit-background-clip: text; background-clip: text; -webkit-text-fill-color: transparent;
    filter: drop-shadow(0 0 10px rgba(63,123,255,.8));
  }
  .neon-rule { position: absolute; left: 52px; width: 729px; height: 3px; }
  .neon-rule.warm { top: 498px; background: linear-gradient(90deg, var(--neon-red), var(--neon-orange)); box-shadow: 0 0 10px var(--neon-red); }
  .neon-rule.cool { top: 677px; background: var(--neon-blue); box-shadow: 0 0 10px var(--neon-blue); }

  .venue {
    position: absolute; left: 94px; top: 704px;
    color: var(--white); font-weight: 400; font-size: 26px;
    letter-spacing: 7px; line-height: 39px; text-transform: uppercase;
  }

  .info-rule { position: absolute; background: var(--white); }
  .info-rule.top { left: 52px; top: 795px; width: 439px; height: 2px; }
  .info-rule.bottom { left: 52px; top: 1074px; width: 335px; height: 2px; }
  .info-rule.divider { left: 259px; top: 796px; width: 2px; height: 279px; }

  .schedule { position: absolute; left: 52px; top: 810px; width: 207px; text-align: center; }
  .schedule svg { display: block; margin: 0 auto; }
  .schedule .label { color: var(--amber); font-weight: 300; font-size: 26px; line-height: 34px; }
  .schedule .time { color: var(--white); font-weight: 300; font-size: 26px; line-height: 34px; }
  .schedule .gap { height: 14px; }

  .website {
    position: absolute; left: 52px; top: 1090px;
    font-family: "Josefin Sans", sans-serif; font-weight: 300; font-size: 17px;
    letter-spacing: 3px; color: var(--white);
  }
</style>
</head>
<body>
  <main class="poster">
    <div class="wall-photo" role="img" aria-label="Photo of a dark brick wall with the shadow of a singer and a splash of drink"></div>
    <div class="studio-mic-photo" role="img" aria-label="Photo of a silver studio microphone"></div>
    <div class="glass-mic-photo" role="img" aria-label="Photo of a wine glass with violet light beside a blue microphone and a warm bokeh light"></div>

    <div class="brand-mark"><span class="brand-name">Copper<br>Lantern</span></div>

    <h1 class="title title-top">Harbour</h1>
    <div class="neon-rule warm"></div>
    <h2 class="title title-bottom">Hours</h2>
    <div class="neon-rule cool"></div>

    <p class="venue">Venue: Copper Lantern<br>218-222 Marlow Rd Preston</p>

    <div class="info-rule top"></div>
    <div class="info-rule divider"></div>
    <div class="info-rule bottom"></div>

    <section class="schedule">
      <svg width="40" height="40" viewBox="0 0 40 40" aria-hidden="true">
        <g fill="none" stroke="#f2a23a" stroke-width="2">
          <path d="M6 8 H30 L18 22 Z"/>
          <path d="M18 22 V35 M11 35 H25"/>
          <circle cx="31" cy="8" r="5"/>
        </g>
      </svg>
      <p class="label">Drink Specials:</p>
      <p class="time">3:00 pm - 5:00pm</p>
      <div class="gap"></div>
      <svg width="38" height="38" viewBox="0 0 38 38" aria-hidden="true">
        <g fill="#f2a23a">
          <path d="M12 6 L32 2 V6 L14 10 Z"/>
          <rect x="12" y="6" width="2.5" height="22"/>
          <rect x="29.5" y="2" width="2.5" height="22"/>
          <ellipse cx="9" cy="29" rx="5" ry="4"/>
          <ellipse cx="27" cy="25" rx="5" ry="4"/>
        </g>
      </svg>
      <p class="label">Live Music:</p>
      <p class="time">4:30pm -6:30pm</p>
    </section>

    <p class="website">www.copperlantern.com.au</p>
  </main>
</body>
</html>
```